Car transport business

We need a new business card design. Attached is our old card sample. I would just like to adjust the logo colors (blue and red) to be brighter. I changed my name to the brighter red and the word dispatcher to a brighter blue as an example. But you can adjust those colors further. And then perhaps you can use the same colors for the card design but use your imagination.

As a suggestion so the card stands out I would like to add a clip art of car carrier truck. Attached are examples of that as well

```html
<!DOCTYPE html>
<html lang="en">
<head>
<meta charset="utf-8">
<title>Summit Haul — Business Card</title>
<link rel="stylesheet" href="https://fonts.googleapis.com/css2?family=Arimo:wght@400;700&display=swap">
<style>
  :root {
    --backdrop: #2b2b2d;
    --card: #1b1c1e;
    --blue: #1f6fd1;
    --red: #ee1c25;
    --white: #f2f2f2;
    --rule: #55575b;
    --pattern-top: #3a3b3e;
    --pattern-bottom: #1f2022;
  }
  * { box-sizing: border-box; margin: 0; padding: 0; }
  html, body {
    width: 1200px; height: 1108px; overflow: hidden;
    background: var(--backdrop);
    font-family: "Arimo", Arial, sans-serif;
  }
  .stage {
    width: 1200px; height: 1108px;
    display: flex; justify-content: center; align-items: center; gap: 70px;
  }
  .card {
    position: relative;
    width: 460px; height: 680px;
    background: var(--card);
    border-radius: 26px;
    box-shadow: 0 18px 40px rgba(0,0,0,.45);
    overflow: hidden;
  }
  /* Front */
  .brand {
    position: absolute; top: 150px; left: 0; right: 0;
    text-align: center;
  }
  .brand-name {
    display: inline-flex; align-items: center; gap: 14px;
    font-weight: 700; font-size: 46px; letter-spacing: 1px;
    color: var(--blue); text-transform: uppercase;
  }
  .brand-dot {
    width: 22px; height: 22px; border-radius: 50%; background: var(--red);
  }
  .brand-tagline {
    margin-top: 10px;
    font-size: 13px; letter-spacing: 4px; text-transform: uppercase;
    color: var(--blue);
  }
  .person {
    position: absolute; top: 430px; left: 0; right: 0; text-align: center;
  }
  .person-name { font-size: 40px; text-transform: uppercase; letter-spacing: 1px; }
  .person-first { color: var(--blue); }
  .person-last { color: var(--red); font-weight: 700; }
  .person-title {
    margin-top: 4px; font-size: 18px; color: var(--white);
    text-transform: uppercase; letter-spacing: .5px;
  }
  .divider { width: 100px; height: 1px; background: var(--rule); margin: 24px auto 22px; }
  .contact { list-style: none; color: var(--white); font-size: 21px; line-height: 1.35; }
  /* Back */
  .pattern { position: absolute; inset: 0;
    background: linear-gradient(160deg, var(--pattern-top), var(--pattern-bottom) 70%); }
  .back-mark {
    position: absolute; right: 80px; bottom: 120px;
    display: flex; align-items: center; gap: 10px;
    font-weight: 700; font-size: 20px; color: var(--blue); text-transform: uppercase;
  }
  .back-mark .brand-dot { width: 14px; height: 14px; }
</style>
</head>
<body>
<main class="stage">
  <section class="card card-front">
    <div class="brand">
      <div class="brand-name"><span class="brand-dot"></span>Summit Haul</div>
      <div class="brand-tagline">The Auto Transport Professionals</div>
    </div>
    <div class="person">
      <div class="person-name"><span class="person-first">Lena</span> <span class="person-last">Marsh</span></div>
      <div class="person-title">Diapatcher</div>
      <div class="divider"></div>
      <ul class="contact">
        <li>555-201-4837</li>
        <li>555-201-7720</li>
        <li>summithaulinc@example.com</li>
      </ul>
    </div>
  </section>
  <section class="card card-back">
    <div class="pattern" role="img" aria-label="Repeating tone-on-tone brand pattern across the card back"></div>
    <div class="back-mark"><span class="brand-dot"></span>Summit Haul</div>
  </section>
</main>
</body>
</html>
```